Harrowgate Estates Business Card for Apartment Buildings

Create business cards for resident managers who run apartment buildings. The audience is the public who are searching for apartment rentals, and current residents who live at the apartment building. Key design element will be incorporating the company logo, however, the logo cannot dominate. The building name and manager name are more important than the logo. Current business card design leaves little room for copy, so we may need to reduce the size on the current card to allow for more space for copy.

Target Market(s)

Adults 18-65 years of age, who are looking for an apartment rental, plus current residents who live at our apartment buildings.

Industry/Entity Type

Property Management

Contact Information for Business Card

A major design element will be use of the company logo. Important property and manager contact information must be part of the design. The size of the logo will need to be reduced to make room for building and manager contact copy.

Font styles to use
Sans Serif

Colors
3176b5
000000
959595
ffffff

Requirements
Must have
• 1) Incorporate the company logo.
• 2) Use the company colors (dark blue, black/grey, over white).
• 3) FEATURE THE BUILDING NAME
• 4) FEATURE THE MANAGER NAME
• 5) The company name is less important than BUILDING and MANAGER
• 6) Manager contact information
• **SEE ATTACHED CREATIVE BRIEF**
Nice to have
• 1) Back of card logo watermark
• 2) Ability to write notes on back of carfd
Should not have
• Avoid letting the company logo dominate the card, the building name and manager are more important than the company logo.

```html
<!DOCTYPE html>
<html lang="en">
<head>
<meta charset="utf-8">
<title>Harrowgate Estates – Resident Manager Card</title>
<link rel="stylesheet" href="https://fonts.googleapis.com/css2?family=Arimo:wght@400;700&display=swap">
<style>
  :root {
    --brand-blue: #0e6ca8;
    --charcoal: #47474a;
    --stage: #e6e7e9;
    --card: #ffffff;
    --card-edge: #c9cacc;
    --faint: #f2f3f5;
    --white: #ffffff;
  }
  * { box-sizing: border-box; margin: 0; padding: 0; }
  html, body { width: 1200px; height: 1200px; overflow: hidden; }
  body {
    background: var(--stage);
    font-family: "Arimo", Arial, sans-serif;
    position: relative;
  }
  .card {
    position: absolute;
    left: 257px;
    width: 686px;
    height: 393px;
    background: var(--card);
    border: 1px solid var(--card-edge);
    overflow: hidden;
  }
  .card--front { top: 182px; }
  .card--back { top: 645px; }

  .brand-mark {
    position: absolute;
    left: 37px;
    top: 112px;
    width: 230px;
    height: 230px;
    border-radius: 50%;
    background: var(--faint);
  }
  .wordmark {
    position: absolute;
    left: 297px;
    top: 36px;
    color: var(--brand-blue);
    font-weight: 700;
    font-size: 30px;
    line-height: 1;
    letter-spacing: -0.5px;
  }
  .wordmark__sub {
    display: block;
    margin-top: 4px;
    font-size: 16px;
    letter-spacing: 3.4px;
  }
  .manager {
    position: absolute;
    left: 297px;
    top: 116px;
  }
  .manager__name {
    color: var(--brand-blue);
    font-size: 28px;
    font-weight: 400;
    line-height: 1.1;
  }
  .manager__title {
    color: var(--charcoal);
    font-size: 13px;
    margin-top: 3px;
  }
  .info-band {
    position: absolute;
    left: 256px;
    top: 178px;
    right: 0;
    height: 183px;
    background: var(--brand-blue);
    color: var(--white);
  }
  .info-band::before {
    content: "";
    position: absolute;
    left: 58px;
    top: -8px;
    border-left: 9px solid transparent;
    border-right: 9px solid transparent;
    border-bottom: 8px solid var(--brand-blue);
  }
  .property {
    position: absolute;
    left: 41px;
    top: 34px;
  }
  .property__name { font-size: 18.5px; line-height: 1.1; }
  .property__address { font-size: 14px; margin-top: 3px; }
  .contacts {
    position: absolute;
    top: 99px;
    list-style: none;
    font-size: 13px;
    line-height: 16.5px;
  }
  .contacts--phones { left: 41px; }
  .contacts--online { left: 190px; }
  .contacts li { display: flex; align-items: center; gap: 6px; }
  .contacts li.gap { height: 16.5px; }
  .contacts svg { width: 10px; height: 10px; fill: var(--white); flex: none; }

  .watermark {
    position: absolute;
    left: 12px;
    top: 12px;
    width: 310px;
    height: 370px;
    border-radius: 50%;
    background: var(--faint);
  }
  .back-brand {
    position: absolute;
    right: 36px;
    top: 296px;
    text-align: right;
  }
  .back-brand__name {
    color: var(--brand-blue);
    font-weight: 700;
    font-size: 23px;
    line-height: 1;
    letter-spacing: -0.3px;
  }
  .back-brand__url {
    margin-top: 14px;
    color: var(--charcoal);
    font-size: 15px;
    letter-spacing: 0.6px;
  }
  .back-brand__url strong { color: var(--brand-blue); font-weight: 700; }
</style>
</head>
<body>
  <section class="card card--front">
    <div class="brand-mark" aria-hidden="true"></div>
    <div class="wordmark">HARROWGATE<span class="wordmark__sub">ESTATES</span></div>
    <div class="manager">
      <h1 class="manager__name">Marisol Dunbar</h1>
      <p class="manager__title">Resident Manager</p>
    </div>
    <div class="info-band">
      <div class="property">
        <h2 class="property__name">Linden Court Apartments</h2>
        <p class="property__address">2480 Cedar Row, Fairview, CA 92817</p>
      </div>
      <ul class="contacts contacts--phones">
        <li><svg viewBox="0 0 10 10"><path d="M1 3.5C1 2 3 1.5 5 1.5S9 2 9 3.5V4.5H7V3.5H3V4.5H1Z"/><rect x="2" y="5" width="6" height="4" rx="1"/></svg>555-201-4830</li>
        <li><svg viewBox="0 0 10 10"><path d="M3 0.5h4a0.8 0.8 0 0 1 0.8 0.8v7.4a0.8 0.8 0 0 1-0.8 0.8h-4a0.8 0.8 0 0 1-0.8-0.8V1.3A0.8 0.8 0 0 1 3 0.5ZM3.2 1.6v6.2h3.6V1.6Z"/></svg>555-372-9146</li>
        <li><svg viewBox="0 0 10 10"><rect x="3" y="0.5" width="4" height="4"/><rect x="0.5" y="4.5" width="9" height="5" rx="0.8"/></svg>555-618-2075</li>
      </ul>
      <ul class="contacts contacts--online">
        <li><svg viewBox="0 0 10 10"><path d="M0.5 2h9v6.5h-9ZM1.2 2.6 5 5.6 8.8 2.6" stroke="#0e6ca8" stroke-width="0.8"/></svg>marisol@harrowgateest.com</li>
        <li class="gap"></li>
        <li><svg viewBox="0 0 10 10"><circle cx="5" cy="5" r="4.3"/><path d="M0.7 5h8.6M5 0.7c2 2.4 2 6.2 0 8.6M5 0.7c-2 2.4-2 6.2 0 8.6" stroke="#0e6ca8" stroke-width="0.7" fill="none"/></svg>www.harrowgateest.com</li>
      </ul>
    </div>
  </section>

  <section class="card card--back">
    <div class="watermark" aria-hidden="true"></div>
    <div class="back-brand">
      <div class="back-brand__name">HARROWGATE ESTATES</div>
      <p class="back-brand__url">www.<strong>harrowgateest</strong>.com</p>
    </div>
  </section>
</body>
</html>
```